Home Design company focused on remodel and enhancement of kitchens and bathroorms

I already have a logo designed by ArtHarbor, I now need a design for my business cards.
The company is in the remodeling and enhancement industry for homes, focusing on kitchens and bathrooms, however, we can remodel or enhance every room in a home, an office space, etc.

The company's name is VELMOR HOME DESIGN, LLC

We'll focus on clients in the Rio Grande Valley, Texas. Primarily McAllen, Edinburg, Pharr, Mission, Brownsville and South Padre Island.

The design on the business card should transmit reliability, professionalism anda bit of upscale design.

The logo is in black and white, and would like to keep it that way.

The information that needs to be printed in the business cards is:
Company's name: Velmor Home Design
Company's Logo (attached)
My name: Noel Bramwit
Address, phone and email:
2715 N Parkline Road, Ste 348
McAllen, TX 78501
(956) 555 0187
nbramwit@velmordesign.example
Website: velmordesign.example

```html
<!DOCTYPE html>
<html lang="en">
<head>
<meta charset="utf-8">
<title>Velmor Home Design – Business Cards</title>
<link href="https://fonts.googleapis.com/css2?family=Lato:wght@400;700&display=swap" rel="stylesheet">
<style>
  :root {
    --bg: #e6e6e6;
    --card: #ffffff;
    --ink: #111111;
    --frame: #000000;
    --tab: #bdbcbc;
  }
  * { box-sizing: border-box; margin: 0; padding: 0; }
  html, body { width: 1200px; height: 801px; overflow: hidden; }
  body {
    background: var(--bg);
    font-family: "Lato", Arial, sans-serif;
    color: var(--ink);
    position: relative;
  }
  .card {
    position: absolute;
    left: 352px;
    width: 529px;
    height: 302px;
    background: var(--card);
    border: 10px solid var(--frame);
  }
  .card--front { top: 43px; }
  .card--back { top: 418px; }

  .holder-name {
    position: absolute;
    left: 39px; top: 40px;
    font-size: 23px;
    font-weight: 400;
    letter-spacing: 0.3px;
  }
  .holder-rule {
    position: absolute;
    left: 39px; top: 77px;
    width: 31px; height: 2px;
    background: var(--ink);
  }
  .company {
    position: absolute;
    left: 39px; top: 156px;
    font-size: 14px;
    font-weight: 700;
    letter-spacing: 1px;
  }
  .address {
    position: absolute;
    left: 39px; top: 181px;
    font-size: 9px;
    font-weight: 700;
    letter-spacing: 0.5px;
  }
  .contact-list {
    position: absolute;
    left: 39px; top: 210px;
    list-style: none;
  }
  .contact-list li {
    display: flex;
    align-items: center;
    height: 18.5px;
    font-size: 9.5px;
    font-weight: 700;
  }
  .contact-list li.phone { font-size: 11.5px; height: 19px; }
  .contact-list svg { width: 11px; height: 11px; margin-right: 8px; flex: none; }

  .brand-tab {
    position: absolute;
    left: 381px; top: 189px;
    width: 90px; height: 113px;
    background: var(--tab);
    display: flex;
    align-items: center;
    justify-content: center;
    padding-top: 16px;
    font-size: 12px;
    font-weight: 700;
    letter-spacing: 1px;
    color: var(--ink);
  }

  .brand-lockup {
    position: absolute;
    right: 28px; top: 202px;
    display: flex;
    align-items: center;
    gap: 12px;
  }
  .brand-lockup .mark-square {
    width: 34px; height: 34px;
    background: var(--ink);
  }
  .brand-lockup .brand-name {
    font-size: 12.5px;
    font-weight: 400;
    letter-spacing: 2.4px;
    line-height: 13px;
  }
</style>
</head>
<body>

  <section class="card card--front" aria-label="Business card front">
    <h1 class="holder-name">NOEL BRAMWIT</h1>
    <div class="holder-rule"></div>
    <p class="company">VELMOR HOME DESIGN</p>
    <p class="address">2715 N PARKLINE ROAD, STE 348, MCALLEN, TX 78501</p>
    <ul class="contact-list">
      <li class="phone">
        <svg viewBox="0 0 24 24" aria-hidden="true"><path fill="currentColor" d="M6.6 10.8a15.1 15.1 0 0 0 6.6 6.6l2.2-2.2c.3-.3.7-.4 1-.2 1.1.4 2.3.6 3.6.6.6 0 1 .4 1 1V20c0 .6-.4 1-1 1A17 17 0 0 1 3 4c0-.6.4-1 1-1h3.5c.6 0 1 .4 1 1 0 1.3.2 2.5.6 3.6.1.3 0 .7-.2 1z"/></svg>
        (956) 555 0187
      </li>
      <li>
        <svg viewBox="0 0 24 24" aria-hidden="true" fill="none" stroke="currentColor" stroke-width="2"><circle cx="12" cy="12" r="10"/><path d="M2 12h20M12 2c3 3 3 17 0 20M12 2c-3 3-3 17 0 20"/></svg>
        www.velmordesign.example
      </li>
      <li>
        <svg viewBox="0 0 24 24" aria-hidden="true" fill="none" stroke="currentColor" stroke-width="2"><rect x="2" y="5" width="20" height="14"/><path d="M2 5l10 8 10-8"/></svg>
        nbramwit@velmordesign.example
      </li>
    </ul>
    <div class="brand-tab">VELMOR</div>
  </section>

  <section class="card card--back" aria-label="Business card back">
    <div class="brand-lockup">
      <span class="mark-square" aria-hidden="true"></span>
      <span class="brand-name">VELMOR<br>HOME<br>DESIGN</span>
    </div>
  </section>

</body>
</html>
```